Tranquil Pathway Business Card

Logo attached. (will be printing onto thick white/off white textured card)

Double sided business card for two Therapists working at Tranquil Pathway.

Require one design, but with different name and mobile numbers on each card.

Target Market(s)

Medical, Health

Industry/Entity Type

Business

Contact Information for Business Card

Need one business card design, but a separate card for each person - Colin Marchetti and Marieke de Boeckx.

FRONT OF CARD

Logo

Name (Colin Marchetti on one card, Marieke de Boeckx on the other)
Professional Clinical Hypnotherapist

Consulting Rooms (Near Lindqvist Hospital)
482 Brackenfield Road
Dunmore VIC 3987

Colin@TranquilPathway.example.au OR Marieke@TranquilPathway.example.au

Mobile: 0455 872 604 (for Colin) OR
Mobile: 0467 290 518 (for Marieke)

BACK OF CARD

Logo

Website: www.TranquilPathway.example.au

Phone: 1300 958 471

Requirements
Must have
• Text and logo only. No additiional graphics.

```html
<!DOCTYPE html>
<html lang="en">
<head>
<meta charset="utf-8">
<title>Marieke de Boeckx – Business Card</title>
<link rel="stylesheet" href="https://fonts.googleapis.com/css2?family=Jost:wght@300;400;600;700&display=swap">
<style>
  :root {
    --navy: #222a5f;
    --band: #666766;
    --paper: #ffffff;
    --band-text: #ffffff;
  }
  html, body {
    margin: 0;
    padding: 0;
    overflow: hidden;
    background: var(--paper);
  }
  .card {
    position: relative;
    width: 1200px;
    height: 686px;
    background: var(--paper);
    overflow: hidden;
    font-family: "Jost", "Century Gothic", sans-serif;
  }
  .card__name {
    position: absolute;
    top: 78px;
    left: 0;
    width: 100%;
    margin: 0;
    text-align: center;
    font-weight: 300;
    font-size: 52px;
    line-height: 1;
    font-variant: small-caps;
    letter-spacing: 0.5px;
    color: var(--navy);
  }
  .card__band {
    position: absolute;
    top: 219px;
    left: 0;
    width: 100%;
    height: 172px;
    background: var(--band);
    display: flex;
    align-items: center;
    justify-content: center;
  }
  .card__title {
    margin: 0;
    font-weight: 600;
    font-size: 50px;
    font-variant: small-caps;
    letter-spacing: 1px;
    color: var(--band-text);
  }
  .contact {
    position: absolute;
    top: 472px;
    left: 326px;
    margin: 0;
    padding: 0;
    list-style: none;
    color: var(--navy);
    font-weight: 700;
    font-size: 28px;
    font-variant: small-caps;
    line-height: 36.5px;
  }
  .contact__item {
    display: flex;
    align-items: center;
    white-space: nowrap;
  }
  .contact__icon {
    width: 30px;
    height: 24px;
    margin-right: 12px;
    flex: none;
  }
  .contact__phone {
    font-variant: normal;
  }
</style>
</head>
<body>
  <main class="card">
    <h1 class="card__name">Marieke de Boeckx</h1>
    <div class="card__band">
      <h2 class="card__title">Professional Clinical Hypnotherapist</h2>
    </div>
    <ul class="contact">
      <li class="contact__item">Consulting Rooms (Near Lindqvist Hospital)</li>
      <li class="contact__item">482 Brackenfield Road, Dunmore, Vic 3987</li>
      <li class="contact__item">
        <svg class="contact__icon" viewBox="0 0 30 24" aria-hidden="true">
          <rect x="1" y="2" width="28" height="20" fill="none" stroke="currentColor" stroke-width="1.6"/>
          <rect x="22" y="4" width="4" height="4" fill="currentColor"/>
          <line x1="10" y1="12" x2="20" y2="12" stroke="currentColor" stroke-width="1.4"/>
          <line x1="8" y1="15" x2="20" y2="15" stroke="currentColor" stroke-width="1.4"/>
          <line x1="8" y1="18" x2="20" y2="18" stroke="currentColor" stroke-width="1.4"/>
        </svg>
        Marieke@TranquilPathway.example.au
      </li>
      <li class="contact__item contact__phone">
        <svg class="contact__icon" viewBox="0 0 30 24" aria-hidden="true">
          <circle cx="13" cy="12" r="10.5" fill="none" stroke="currentColor" stroke-width="1.6"/>
          <path d="M9 6 Q7 7 7.5 11 Q9 16 13 18 Q15 18.5 16 17 L14 14.5 L12.5 15 Q10.5 13 10 10.5 L11.5 9.5 Z" fill="currentColor"/>
        </svg>
        0467 290 518
      </li>
    </ul>
  </main>
</body>
</html>
```